Hardcore nerd needs to stand out in a sea of dull Defence business cards

Wombat Devices is a new Australian consulting engineering company that turns research and theory into practical systems. No evangelistic fluff, just mathematics and physics into electronic and optical circuits for consumer products, scientific research or Defence applications.

We already have a recognised logo (provided) which is often dark blue/black on a light background but we're open to other combinations. (Us engineers tend to have limited aesthetic imagination :)

Some of our recent products have included:
* Instrumentation for electrical testing,
* Radar jammers,
* GPS antenna design,
* Satellite tracking systems,
* High power lasers

We're open to both single and double-sided designs - happy to be convinced either way.

P.S. Another group is working on the web page, so - alas - our web site is currently of no use for images/ideas...

Target Market(s)

Engineering managers,
Scientists

Contact Information for Business Card

Dr Colin Marsh
R&D Engineer

colin@wombatdevicesco.com.au
0427 563 210

PO Box XXX (to be confirmed)
Banks ACT 2913
Australia

Font styles to use
Serif
Sans Serif

Colors

Designer to choose colors to be used in the design.

Requirements
Must have
• My contact details!
• I've had many (great) "bold and plain" designs submitted already, so feel free to be artistically creative :)
• Happy to take advice re fonts/colours/printability etc.
Nice to have
• I'm not sure if "lists" are more at home on a CV than a business card, but representative services include:
• Applied electromagnetics
• RF and high speed electronics
• Signal and image processing
• Electro-optical and laser systems
• Concept-to-prototype design services
• If you're considering double sided cards, then often measuring/alignment grids/rulers feature on the back of similar cards.
• e.g. https://www.lumoptix-example.com/newgrouppage9.cfm?objectgroup_id=4815
• https://www.lumoptix-example.com/newgrouppage9.cfm?objectgroup_ID=4817
• ..or even a "Smith chart" (google will return lots)
• Generic images to represent a capability might work - googling images associated with keyword for each of these areas might help:
• - "passive radar", "phased array", "fdtd", "vircator"
• RF and high speed electronic design
• - "smith chart", "microstrip circuits", "dimensioned drawing", "electronic schematic"
• - "dft", "iir filter"
• - "optical cavity". "laser energy level diagram"
• Background/watermarked images outlines/wireframes/schematics would probably look OK.
Should not have
• If a list of projects/services is provided, it is important not to make the client feel that this is "all" the company can do. Engineering design is a creative discipline (like graphics :)
• Please, no stock "military" snaps like planes, missiles, etc!

```html
<!DOCTYPE html>
<html lang="en">
<head>
<meta charset="utf-8">
<title>Wombat Devices – Business Card</title>
<link href="https://fonts.googleapis.com/css2?family=Lato:wght@400;700;900&display=swap" rel="stylesheet">
<style>
  :root {
    --navy: #232b63;
    --paper: #ffffff;
    --ink-soft: #2b2f4a;
    --stage: #2a2a2c;
  }
  * { box-sizing: border-box; margin: 0; padding: 0; }
  html, body {
    width: 1200px; height: 970px; overflow: hidden;
    background: var(--stage);
    font-family: "Lato", sans-serif;
  }
  .card {
    position: absolute;
    width: 640px; height: 366px;
    box-shadow: 0 12px 30px rgba(0,0,0,.45);
  }
  /* Front */
  .card-front { left: 80px; top: 70px; background: var(--paper); color: var(--navy); }
  .accent-bar {
    position: absolute; left: 0; top: 160px;
    width: 20px; height: 46px; background: var(--navy);
  }
  .person { position: absolute; left: 52px; top: 156px; }
  .person-name { font-size: 34px; font-weight: 900; line-height: 1; letter-spacing: -0.3px; }
  .person-title { font-size: 15px; font-weight: 400; color: var(--ink-soft); margin-top: 6px; }
  .address {
    position: absolute; left: 86px; top: 232px;
    font-size: 15px; line-height: 1.25; color: var(--ink-soft);
  }
  .contacts {
    position: absolute; left: 86px; top: 282px;
    list-style: none; font-size: 15px; color: var(--ink-soft);
  }
  .contacts li { display: flex; align-items: center; gap: 10px; height: 22px; }
  .contacts svg { width: 16px; height: 16px; fill: var(--navy); flex: none; }
  .brand-front {
    position: absolute; right: 60px; top: 60px; width: 200px;
    display: flex; flex-direction: column; align-items: center; gap: 16px;
  }
  .brand-dot { width: 150px; height: 150px; border-radius: 50%; background: var(--navy); }
  .brand-name-front { font-size: 24px; font-weight: 900; color: var(--navy); letter-spacing: 1px; text-transform: uppercase; text-align: center; }
  /* Back */
  .card-back { left: 480px; top: 520px; background: var(--navy); color: var(--paper); }
  .brand-back {
    position: absolute; left: 150px; top: 60px;
    display: flex; align-items: center; gap: 18px;
  }
  .brand-back .brand-dot { width: 70px; height: 70px; background: var(--paper); }
  .brand-name-back { font-size: 30px; font-weight: 900; letter-spacing: 1.5px; text-transform: uppercase; line-height: 1; }
  .services {
    position: absolute; left: 150px; top: 170px;
    list-style: none; font-size: 20px; line-height: 30px;
  }
  .services li { display: flex; align-items: center; gap: 14px; }
  .services li::before {
    content: ""; width: 12px; height: 12px; border-radius: 50%;
    background: var(--paper); flex: none;
  }
</style>
</head>
<body>
  <section class="card card-front">
    <div class="accent-bar"></div>
    <div class="person">
      <h1 class="person-name">Dr Colin Marsh</h1>
      <p class="person-title">R&amp;D Engineer</p>
    </div>
    <p class="address">PO Box XXX<br>Banks ACT 2913, Australia</p>
    <ul class="contacts">
      <li>
        <svg viewBox="0 0 24 24" aria-hidden="true"><path d="M6.6 10.8a15.1 15.1 0 0 0 6.6 6.6l2.2-2.2c.3-.3.7-.4 1-.2 1.1.4 2.3.6 3.6.6.6 0 1 .4 1 1V20c0 .6-.4 1-1 1A17 17 0 0 1 3 4c0-.6.4-1 1-1h3.5c.6 0 1 .4 1 1 0 1.3.2 2.5.6 3.6.1.3 0 .7-.2 1z"/></svg>
        0427 563 210
      </li>
      <li>
        <svg viewBox="0 0 24 24" aria-hidden="true"><path d="M2 5h20v14H2z M3.5 6.5 12 13l8.5-6.5" fill="none" stroke="currentColor" stroke-width="0"/><path d="M2 5h20v14H2V5zm2 2v.3l8 5.4 8-5.4V7H4z"/></svg>
        colin@wombatdevicesco.com.au
      </li>
      <li>
        <svg viewBox="0 0 24 24" aria-hidden="true"><path d="M12 2a10 10 0 1 0 0 20 10 10 0 0 0 0-20zm7.9 9h-3.9a15 15 0 0 0-1.4-6.3A8 8 0 0 1 19.9 11zM12 4c1 1.3 1.9 3.8 2 7h-4c.1-3.2 1-5.7 2-7zM9.4 4.7A15 15 0 0 0 8 11H4.1a8 8 0 0 1 5.3-6.3zM4.1 13H8a15 15 0 0 0 1.4 6.3A8 8 0 0 1 4.1 13zM12 20c-1-1.3-1.9-3.8-2-7h4c-.1 3.2-1 5.7-2 7zm2.6-.7A15 15 0 0 0 16 13h3.9a8 8 0 0 1-5.3 6.3z"/></svg>
        www.wombatdevicesco.com.au
      </li>
    </ul>
    <div class="brand-front">
      <div class="brand-dot"></div>
      <p class="brand-name-front">Wombat Devices</p>
    </div>
  </section>

  <section class="card card-back">
    <div class="brand-back">
      <div class="brand-dot"></div>
      <p class="brand-name-back">Wombat Devices</p>
    </div>
    <ul class="services">
      <li>Instrumentation for electrical testing</li>
      <li>Radar jammers</li>
      <li>GPS antenna design</li>
      <li>Satellite tracking systems</li>
      <li>High power lasers</li>
    </ul>
  </section>
</body>
</html>
```